Mediakit / brochure for Dutch Travel Blog

About our company:
• Bolderwijk.nl is a Travel- & influence network for independent travellers, outdoor geeks, culture lovers & adventure seekers.
• We don’t sell trips by ourself, we inspire other to travel.
• It’s all about travel inspiration.

About the media kit / brochure:
• The media kit itself must be a travel experience / inspiration.
• Colourful and clean design.
• Use the colours of our new logo
• Use our icons (marker, worldmap) in the design
• Use the style of our website.
• All the text in the media kit must be adjustable by us
• Page format: A4
• Number of pages: 6
• It must be printable as a brochure (for presentations)
• We also need a .pdf version of the brochure (for emailing it to our partners)
• Logo kit added: (1a) + (1b) + (1c) Logo sourcefile

Content of the media kit / brochure
• 6 pages
o (1) Front page
o (2) About Us
o (3) Stats / Companies work with
o (4) Advertising
o (5) Back page
o (6) Our contributors

• Example is attached: (2) example of a brochure with 5 pages A4 (don’t like the design of this example for our media kit, but just to show the idea of the 5 pages).

Maybe use a big travel photo that covers all pages?

For detailed information, I attached the document 'Design brochure Bolderwijk (version 2)'.
Updates

Hello designers,Small update for the Cover Page:- Please use one of the images from the attachment I added in the Brief Design: "URL of images for cover.txt"- Use this text "Travel- & influence network for independent travelers, outdoor geeks, culture lovers & adventure seekers."- Add the text MEDIA KIT (remove "2017: )Thanks.Hendrik Added Thursday, January 5, 2017

Target Market(s)

The mediakit / brochure is for our partners (travel organisations, airline companies, PR companies and big brands like Pale Timber Co and Vesko).

And the readers of our website are independent travellers, outdoor geeks and adventure seekers. So the theme of the Mediakit must be 'travel inspiration'.

Industry/Entity Type

Travel Industry

Requirements
Must have
• • The media kit itself must be a travel experience / inspiration.
• • Colourful and clean design.
• • Use the colours of our new logo
• • Use our icons (marker, worldmap) in the design
• • Use the style of our website.
• • All the text in the media kit must be adjustable by us
• • Page format: A4
• • Number of pages: 6
• • It must be printable as a brochure (for presentations)
• • We also need a .pdf version of the brochure (for emailing it to our partners)

```html
<!DOCTYPE html>
<html lang="en">
<head>
<meta charset="utf-8">
<title>Bolderwijk Media Kit</title>
<link href="https://fonts.googleapis.com/css2?family=Montserrat:ital,wght@0,400;0,600;0,700;1,600;1,700&family=Open+Sans:wght@400;600;700&family=Caveat:wght@600&display=swap" rel="stylesheet">
<style>
:root{
  --pink:#e6197e;
  --cyan:#1aa3d4;
  --yellow:#f2c318;
  --green:#8cc63f;
  --orange:#f39a1f;
  --purple:#8e3ea8;
  --ink:#3d3d3d;
  --muted:#7a7a7a;
  --paper:#ffffff;
  --stage:#e8e8e9;
  --tint:#f3f6d6;
}
*{box-sizing:border-box;margin:0;padding:0}
html,body{width:1200px;height:800px;overflow:hidden;background:var(--stage)}
body{font-family:"Open Sans",Arial,sans-serif;color:var(--ink);position:relative}
.spread{position:absolute;left:195px;width:810px;height:382px;display:flex;box-shadow:0 4px 14px rgba(0,0,0,.18)}
.spread--outer{top:8px}
.spread--inner{top:402px}
.panel{position:relative;width:270px;height:382px;background:var(--paper);overflow:hidden;border-right:1px solid #eee}
.panel:last-child{border-right:0}
.swoosh{position:absolute;left:0;bottom:0;width:100%;height:70px}
.url{position:absolute;left:0;right:0;bottom:10px;text-align:center;font-size:7px;letter-spacing:2.5px;color:var(--muted)}
.url--dark{color:#555}
h2.section{font-family:Montserrat,sans-serif;font-weight:700;font-size:9px;color:var(--pink);letter-spacing:.5px;text-transform:uppercase}
h3.sub{font-family:Montserrat,sans-serif;font-weight:600;font-size:6.5px;color:var(--green);text-transform:uppercase}
p.body{font-size:5.6px;line-height:1.45;color:var(--ink)}

/* contributors */
.team-title{position:absolute;top:26px;left:20px;right:20px;text-align:center;font-family:Montserrat,sans-serif;font-style:italic;font-weight:700;font-size:9.5px;color:var(--pink);line-height:1.25}
.team{position:absolute;top:62px;left:14px;right:14px;display:flex;flex-wrap:wrap;justify-content:center;gap:8px 10px}
.member{width:52px;text-align:center}
.avatar{width:40px;height:40px;border-radius:50%;margin:0 auto;background:radial-gradient(circle at 40% 35%,#e7c9a8,#9a7357)}
.member-name{font-size:4.6px;color:var(--muted);margin-top:2px;font-style:italic}
.team-wash{position:absolute;top:40px;left:8px;width:250px;height:210px;border-radius:50%;background:radial-gradient(ellipse,rgba(230,25,126,.08),rgba(26,163,212,.06) 60%,transparent 72%)}
.mission{position:absolute;left:18px;right:18px;bottom:34px;text-align:center;font-family:Montserrat,sans-serif;font-style:italic;font-weight:600;font-size:7px;line-height:1.35;color:#6a6a6a}

/* contact */
.panel--contact{background:var(--tint)}
.city-wash{position:absolute;left:0;top:60px;width:100%;height:210px;background:linear-gradient(180deg,rgba(255,255,255,0),rgba(214,226,160,.7) 45%,rgba(190,214,196,.6) 75%,rgba(243,246,214,0))}
.contact-title{position:absolute;top:28px;left:26px;font-family:Montserrat,sans-serif;font-weight:600;font-size:7.5px;letter-spacing:.6px;color:#555;text-transform:uppercase}
.persons{position:absolute;top:46px;left:26px;right:24px;list-style:none}
.person{display:flex;gap:8px;align-items:flex-start;padding:4px 0;border-bottom:1px solid var(--yellow)}
.person svg{width:10px;height:10px;flex:none}
.person b{display:block;font-weight:400;font-size:6px;color:#555}
.person span{font-size:5.4px;color:#666}
.socials{position:absolute;top:258px;left:26px;list-style:none}
.socials li{display:flex;align-items:center;gap:6px;font-size:7px;color:#444;line-height:10px}
.socials i{width:7px;height:7px;border-radius:50%;border:1px solid var(--pink);display:inline-block}

/* cover */
.panel--cover{background:#fff}
.cover-photo{position:absolute;left:0;top:0;width:100%;height:250px;background:linear-gradient(180deg,#2a2f63 0%,#3f5f7a 25%,#6fc08c 40%,#355a74 58%,#cfd9e3 78%,#8ea4b6 100%)}
.brand{position:absolute;top:20px;left:0;right:0;display:flex;justify-content:center;align-items:center;gap:5px;font-family:Montserrat,sans-serif;font-weight:700;font-size:16px;color:#fff;letter-spacing:.5px}
.brand i{width:9px;height:9px;border-radius:50%;background:#fff;display:inline-block}
.edition{position:absolute;top:150px;right:22px;text-align:right;color:#fff;font-family:Montserrat,sans-serif}
.edition b{display:block;font-size:26px;font-weight:700;line-height:1}
.edition span{font-size:10px;font-weight:600;letter-spacing:.5px}
.colour-bar{position:absolute;top:250px;left:0;width:100%;height:3px;background:linear-gradient(90deg,var(--pink),var(--orange),var(--yellow),var(--green),var(--cyan))}
.tagline{position:absolute;top:272px;left:24px;right:24px;text-align:center;font-family:Montserrat,sans-serif;font-size:8px;line-height:1.4;color:#666}

/* about */
.about-text{position:absolute;top:20px;left:18px;width:158px}
.about-text h2{margin-bottom:8px}
.about-text p{margin-bottom:6px}
.about-photo{position:absolute;left:18px;top:258px;width:158px;height:70px;background:linear-gradient(180deg,#5d6f93,#b89275 55%,#3d4f6a)}
.about-rule{position:absolute;left:40px;width:114px;bottom:26px;height:1px;background:var(--pink)}
.stripes{position:absolute;top:0;left:184px;width:6px;height:100%;background:linear-gradient(180deg,var(--pink),var(--orange),var(--yellow),var(--green),var(--cyan))}
.tower-photo{position:absolute;top:0;left:190px;width:80px;height:100%;background:linear-gradient(180deg,#5e6d8f 0%,#c48b7e 30%,#8a8275 55%,#3a4858 80%,#2c3440 100%)}

/* stats */
.stats{position:absolute;top:18px;left:14px;right:12px}
.stats-cols{display:flex;gap:10px;margin-top:4px}
.stats-col{flex:1}
.gender{display:flex;gap:6px;align-items:center;margin:3px 0}
.gender svg{width:14px;height:18px}
.pct{font-family:Montserrat,sans-serif;font-weight:700;font-size:7px;line-height:1.1}
.pct--pink{color:var(--pink)}.pct--cyan{color:var(--cyan)}
.label{font-size:5px;color:#555;font-weight:600}
.ages{list-style:none;margin-top:2px}
.ages li{display:flex;align-items:center;gap:3px;font-size:4.4px;color:#555;height:6px}
.ages i{display:block;height:4.5px}
.map{margin-top:3px;width:100%;height:32px;background:radial-gradient(ellipse at 30% 50%,#9fd9ec,#cdeef6 55%,#fff 75%)}
.metric{display:flex;align-items:center;gap:5px;margin-top:2px}
.metric b{font-family:Montserrat,sans-serif;font-weight:700;font-size:9px;color:var(--pink)}
.metric small{font-size:4.6px;color:#666;display:block}
.metric i{width:7px;height:7px;background:var(--cyan);display:inline-block;flex:none}
.companies{position:absolute;top:150px;left:14px;right:12px}
.companies h2{margin-bottom:6px}
.partners{display:flex;gap:8px}
.partners > div{flex:1}
.script{font-family:Caveat,cursive;font-weight:600;font-size:10px;color:var(--green);margin:4px 0 2px}
.logos{display:grid;grid-template-columns:1fr 1fr;gap:3px;margin-top:4px}
.logo-box{height:20px;border:1px solid #e4e4e4;display:flex;align-items:center;justify-content:center;gap:3px;font-size:5.6px;font-weight:700;color:#4a4a4a;background:#fff}
.logo-box i{width:4px;height:4px;background:var(--cyan);display:inline-block}
.cta{position:absolute;right:16px;bottom:34px;font-family:Montserrat,sans-serif;font-style:italic;font-weight:700;font-size:10px;color:var(--pink)}

/* advertising */
.ads{position:absolute;top:16px;left:14px;right:12px}
.ads h2{margin-bottom:3px}
.ads-cols{display:flex;gap:8px;margin-top:5px}
.ads-col{flex:1}
.ads-col h4{font-family:Montserrat,sans-serif;font-weight:700;font-size:5.4px;color:var(--pink);margin-top:4px}
.ads-col .lead{font-family:Montserrat,sans-serif;font-weight:700;font-size:6px;color:#333}
.ads p.body{font-size:4.9px}
.pricing{width:100%;border-collapse:collapse;margin-top:3px}
.pricing td{font-size:4.4px;padding:.8px 2px;border-bottom:1px solid #ddd;color:#444}
.pricing td:last-child{text-align:right;white-space:nowrap}
</style>
</head>
<body>

<!-- Outer spread -->
<section class="spread spread--outer">
  <article class="panel panel--team">
    <div class="team-wash"></div>
    <h2 class="team-title">Hi! We're all Bolderwijk and we want to help you travel better…</h2>
    <div class="team">
      <figure class="member"><div class="avatar" role="img" aria-label="Portrait photo of contributor"></div><figcaption class="member-name">Lotte Haans</figcaption></figure>
      <figure class="member"><div class="avatar" role="img" aria-label="Portrait photo of contributor"></div><figcaption class="member-name">Hendrik Mols</figcaption></figure>
      <figure class="member"><div class="avatar" role="img" aria-label="Portrait photo of contributor"></div><figcaption class="member-name">Anke de Wit</figcaption></figure>
      <figure class="member"><div class="avatar" role="img" aria-label="Portrait photo of contributor"></div><figcaption class="member-name">Joost Brink</figcaption></figure>
      <figure class="member"><div class="avatar" role="img" aria-label="Portrait photo of contributor"></div><figcaption class="member-name">Fleur Kamp</figcaption></figure>
      <figure class="member"><div class="avatar" role="img" aria-label="Portrait photo of contributor"></div><figcaption class="member-name">Sem Bakker</figcaption></figure>
      <figure class="member"><div class="avatar" role="img" aria-label="Portrait photo of contributor"></div><figcaption class="member-name">Ilse Verhoef</figcaption></figure>
      <figure class="member"><div class="avatar" role="img" aria-label="Portrait photo of contributor"></div><figcaption class="member-name">Daan Vos</figcaption></figure>
      <figure class="member"><div class="avatar" role="img" aria-label="Portrait photo of contributor"></div><figcaption class="member-name">Noor Smit</figcaption></figure>
      <figure class="member"><div class="avatar" role="img" aria-label="Portrait photo of contributor"></div><figcaption class="member-name">Eva Dekker</figcaption></figure>
    </div>
    <svg class="swoosh" viewBox="0 0 270 70" preserveAspectRatio="none" aria-hidden="true">
      <defs><linearGradient id="sw1" x1="0" x2="1"><stop offset="0" stop-color="#f2c318"/><stop offset=".45" stop-color="#8cc63f"/><stop offset=".75" stop-color="#1aa3d4"/><stop offset="1" stop-color="#e6197e"/></linearGradient></defs>
      <path d="M0 40 C80 10 170 20 270 0 L270 12 C170 34 80 28 0 58 Z" fill="url(#sw1)" opacity=".55"/>
    </svg>
    <p class="mission">World Traveller with the mission to travel endlessly, write about their adventures and provide you with useful tips!</p>
    <div class="url">www.bolderwijk.nl</div>
  </article>

  <article class="panel panel--contact">
    <div class="city-wash" role="img" aria-label="Faded photo of a riverside old town with a church spire"></div>
    <h2 class="contact-title">Contact information</h2>
    <ul class="persons">
      <li class="person"><svg viewBox="0 0 10 10"><circle cx="5" cy="3" r="2.2" fill="#e6197e"/><path d="M1 10 C1 6 9 6 9 10Z" fill="#e6197e"/></svg><div><b>Person Name</b><span>name@bolderwijk.nl</span></div></li>
      <li class="person"><svg viewBox="0 0 10 10"><circle cx="5" cy="3" r="2.2" fill="#e6197e"/><path d="M1 10 C1 6 9 6 9 10Z" fill="#e6197e"/></svg><div><b>Person Name</b><span>name@bolderwijk.nl</span></div></li>
      <li class="person"><svg viewBox="0 0 10 10"><circle cx="5" cy="3" r="2.2" fill="#e6197e"/><path d="M1 10 C1 6 9 6 9 10Z" fill="#e6197e"/></svg><div><b>Person Name</b><span>name@bolderwijk.nl</span></div></li>
    </ul>
    <ul class="socials">
      <li><i></i>Chatterly - chatterly.com/bolderwijk</li>
      <li><i></i>Moodboard - moodboard.com/bolderwijk</li>
      <li><i></i>Reelhub - reelhub.com/bolderwijk</li>
      <li><i></i>Friendsfeed - www.friendsfeed.com/bolderwijk</li>
      <li><i></i>Photolane - photolane.com/bolderwijk</li>
    </ul>
    <div class="url url--dark">www.bolderwijk.nl</div>
  </article>

  <article class="panel panel--cover">
    <div class="cover-photo" role="img" aria-label="Northern lights over snowy mountains and ice floes"></div>
    <div class="brand"><span>BOLDERWIJK</span><i></i></div>
    <div class="edition"><b>2017</b><span>MEDIA KIT</span></div>
    <div class="colour-bar"></div>
    <p class="tagline">Dutch travel- &amp; influence network for independent travellers, outdoor geeks &amp; adventure seekers.</p>
    <div class="url">www.bolderwijk.nl</div>
  </article>
</section>

<!-- Inner spread -->
<section class="spread spread--inner">
  <article class="panel panel--about">
    <div class="about-text">
      <h2 class="section">About us</h2>
      <p class="body">Bolderwijk is leading in travel inspiration in The Netherlands. Our impassioned team of travel journalists, bloggers and youtubers create travel stories about independent &amp; off the beaten track travel, near and afar. Created in 2007, Bolderwijk began as a personal backpack blog that has now turned into an award winning travel platform.</p>
      <p class="body">Our blog is all about providing inspiration for your own journeys no matter how big or small. We love documenting the world around us, seeking out eclectic travel moments and inspiring others to live the life they desire. Our knowledge of the world's most inspiring places is unrivalled.</p>
      <p class="body">The travel stories by Bolderwijk show us that we can conquer the world, get lost in its beauty, and find ourselves wherever our feet (or passport) may take us. We take our readers and fans on a digital journey around the world in search of the beautiful, the unusual, the forgotten and the mundane. Sit down, relax and have a browse of our inspiring travel stories and videos on www.bolderwijk.nl.</p>
    </div>
    <div class="about-photo" role="img" aria-label="Historic building beside a river at dusk"></div>
    <div class="about-rule"></div>
    <div class="url" style="right:94px">www.bolderwijk.nl</div>
    <div class="stripes"></div>
    <div class="tower-photo" role="img" aria-label="Church tower and stone bridge over a river at sunset"></div>
  </article>

  <article class="panel panel--stats">
    <div class="stats">
      <h2 class="section">Statistics</h2>
      <div class="stats-cols">
        <div class="stats-col">
          <h3 class="sub">Audience overview</h3>
          <div class="gender">
            <div><div class="label">Gender</div>
              <svg viewBox="0 0 14 18"><circle cx="3.5" cy="2" r="1.6" fill="#e6197e"/><path d="M1 9 L3.5 4 L6 9 H4.5 V16 H2.5 V9Z" fill="#e6197e"/><circle cx="10.5" cy="2" r="1.6" fill="#1aa3d4"/><rect x="9" y="4" width="3" height="12" fill="#1aa3d4"/></svg>
            </div>
            <div><div class="pct pct--pink">66%</div><div class="pct pct--cyan">34%</div></div>
            <div style="flex:1">
              <div class="label">Ages</div>
              <ul class="ages">
                <li><i style="width:14px;background:#8cc63f"></i>11%</li>
                <li><i style="width:32px;background:#1aa3d4"></i>30%</li>
                <li><i style="width:28px;background:#8e3ea8"></i>26%</li>
                <li><i style="width:19px;background:#e6197e"></i>17%</li>
                <li><i style="width:7px;background:#f39a1f"></i>5%</li>
                <li><i style="width:4px;background:#f2c318"></i>2%</li>
              </ul>
            </div>
          </div>
          <div class="label">Countries visited</div>
          <div class="pct pct--pink">81%</div>
          <div class="map" role="img" aria-label="World map marking visited countries"></div>
        </div>
        <div class="stats-col">
          <h3 class="sub">Traffic</h3>
          <div class="metric"><i style="background:var(--pink)"></i><div><small>Number of unique visitors each month</small><b>115,000</b></div></div>
          <div class="metric"><i></i><div><small>Number of page views each month</small><b style="color:var(--cyan)">240,000</b></div></div>
          <h3 class="sub" style="margin-top:4px">Social media</h3>
          <div class="metric"><i></i><small>Friendsfeed</small><b>30,000</b></div>
          <div class="metric"><i></i><small>Photolane</small><b>5200</b></div>
          <div class="metric"><i></i><small>Chatterly</small><b>7000</b></div>
        </div>
      </div>
    </div>
    <div class="companies">
      <h2 class="section">Companies we work with:</h2>
      <div class="partners">
        <div>
          <p class="body">Wondering how to transform your product from a commodity into an experience? Not sure how to leverage the power of social media and connect with your target demographic? Need help aligning your branding with your company values? Whether you are a tourism board, travel company, property, or product, we can help. We work with more than 100 travel- and brand partners.</p>
          <div class="script">Brand partners</div>
          <p class="body">Bolderwijk reaches a wide audience of travellers passionate about unique experiences and amazing products.</p>
          <div class="logos">
            <div class="logo-box"><i></i>Actioncam Co</div>
            <div class="logo-box">Vesko</div>
            <div class="logo-box">Pale Timber Co</div>
            <div class="logo-box">Routewise</div>
            <div class="logo-box">Roundhouse</div>
          </div>
        </div>
        <div>
          <div class="script" style="margin-top:0">Travel partners</div>
          <p class="body">We have worked with some of the world's top travel companies &amp; destinations to help them achieve their goals through social media promotion.</p>
          <div class="logos">
            <div class="logo-box"><i></i>Aerolune</div>
            <div class="logo-box">Meridian Air</div>
            <div class="logo-box">Tuk Trails</div>
            <div class="logo-box">Isla Sol</div>
            <div class="logo-box">Farefinder</div>
            <div class="logo-box">Lynx Journeys</div>
          </div>
        </div>
      </div>
    </div>
    <svg class="swoosh" viewBox="0 0 270 70" preserveAspectRatio="none" aria-hidden="true">
      <defs><linearGradient id="sw2" x1="0" x2="1"><stop offset="0" stop-color="#e6197e"/><stop offset=".35" stop-color="#f2c318"/><stop offset=".7" stop-color="#8cc63f"/><stop offset="1" stop-color="#1aa3d4"/></linearGradient></defs>
      <path d="M0 62 C90 56 180 52 270 30 L270 46 C180 66 90 70 0 70 Z" fill="url(#sw2)" opacity=".6"/>
    </svg>
    <div class="cta">Let's work together!</div>
  </article>

  <article class="panel panel--ads">
    <div class="ads">
      <h2 class="section">Advertising</h2>
      <p class="body">Bolderwijk has a large online interactive community through its readers and social networks that provides a perfect venue to showcase your brand or destination to a highly engaged online audience of travel enthusiasts. Check out some of the things we can do for you.</p>
      <div class="ads-cols">
        <div class="ads-col">
          <div class="lead">Sponsorship Opportunities</div>
          <h4>Travel Writing</h4>
          <p class="body">Digital storytelling is our core business. We take readers off the beaten path to bustling cities, wild nightlife and unbeatable landscapes.</p>
          <h4>Press &amp; Fam Trips</h4>
          <p class="body">The only thing we love more than experiencing new places is sharing them with our readers. In 2016 our journalists went to Peru, Norway, South Africa, Costa Rica, Thailand and Spitsbergen.</p>
          <h4>Reviews / Sponsorship</h4>
          <p class="body">We love reviews! They give us a chance to let our readers know about unique products for the experiential traveler.</p>
          <h4>Traveldirectory</h4>
          <p class="body">Are you the owner of a small romantic B&amp;B or a cool rafting company? List it in our unique traveldirectory for local attractions, tours and restaurants.</p>
        </div>
        <div class="ads-col">
          <h4>Advertising</h4>
          <p class="body">Advertorials, SEO articles, sidebars, banners, social media promotion. We help your business market its products and grow awareness.</p>
          <h4>Photography</h4>
          <p class="body">Stunning images are one of the best ways to showcase your brand or destination on website and social networks.</p>
          <h4>Travelvlogs</h4>
          <p class="body">Professionally produced and edited videos. Showcase your destination through the eyes of a world traveler!</p>
          <h4>Videography using drones</h4>
          <p class="body">Our state of the art drone footages will blow your mind.</p>
          <div class="lead" style="margin-top:5px">Our Pricing:</div>
          <table class="pricing">
            <tr><td>Traveldirectory</td><td>€ 100 (per year)</td></tr>
            <tr><td>Textlink</td><td>€ 250 (per year)</td></tr>
            <tr><td>Advertorials (max 3 links)</td><td>€ 300</td></tr>
            <tr><td>Sidebars</td><td>Please ask</td></tr>
            <tr><td>Banners</td><td>Please ask</td></tr>
            <tr><td>Social shares - Friendsfeed</td><td>€ 150</td></tr>
            <tr><td>- Photolane</td><td>€ 100</td></tr>
            <tr><td>- Chatterly</td><td>€ 50</td></tr>
            <tr><td>Reviews</td><td>€ 250</td></tr>
            <tr><td>Reelhub video</td><td>€ 250</td></tr>
            <tr><td>Videography using drones</td><td>€ 1.000</td></tr>
          </table>
        </div>
      </div>
    </div>
    <svg class="swoosh" viewBox="0 0 270 70" preserveAspectRatio="none" aria-hidden="true">
      <defs><linearGradient id="sw3" x1="0" x2="1"><stop offset="0" stop-color="#8cc63f"/><stop offset=".5" stop-color="#f2c318"/><stop offset="1" stop-color="#e6197e"/></linearGradient></defs>
      <path d="M0 30 C90 50 180 40 270 56 L270 70 L0 70 Z" fill="url(#sw3)" opacity=".5"/>
    </svg>
  </article>
</section>

</body>
</html>
```